Business Card Design Project

I need a business card designed with these details on the front along with the logo attached on the front.

Address - 518/ 217 Wendlebury st Thornvale
Website - www.brackenhollowmasonry.com.au
Email - delwyn@brackenhollowmasonry.com.au
Fax - 1900 457 618
Mobile - 0471926038
Telephone - 1300517926
Licence number - 847263k

```html
<!DOCTYPE html>
<html lang="en">
<head>
<meta charset="utf-8">
<title>Bracken Hollow Masonry — Business Card</title>
<link rel="stylesheet" href="https://fonts.googleapis.com/css2?family=Cinzel:wght@500&family=Lato:wght@300;400&display=swap">
<style>
  :root {
    --page-bg: #ecebe8;
    --front-light: #e6d8c0;
    --front-mid: #c9b08a;
    --front-dark: #9c7f55;
    --front-ink: #fbf6ec;
    --back-light: #f7f7f6;
    --back-dark: #dcdcdc;
    --back-ink: #4a4540;
    --mark-fill: #b8a78d;
    --card-shadow: rgba(60, 45, 25, 0.25);
  }
  * { box-sizing: border-box; margin: 0; padding: 0; }
  html, body {
    width: 1200px;
    height: 801px;
    overflow: hidden;
    background: var(--page-bg);
  }
  .sheet {
    width: 1200px;
    height: 801px;
    display: flex;
    align-items: center;
    justify-content: center;
    gap: 60px;
  }
  .card {
    position: relative;
    width: 510px;
    height: 312px;
    border-radius: 3px;
    box-shadow: 0 10px 28px var(--card-shadow);
    overflow: hidden;
  }
  .card--front {
    background: linear-gradient(160deg, var(--front-light) 0%, var(--front-mid) 55%, var(--front-dark) 100%);
    color: var(--front-ink);
  }
  .card--back {
    background: linear-gradient(200deg, var(--back-light) 0%, #ececeb 60%, var(--back-dark) 100%);
    color: var(--back-ink);
  }
  .brand {
    position: absolute;
    display: flex;
    align-items: center;
    gap: 12px;
  }
  .brand__square {
    width: 30px;
    height: 30px;
    background: var(--mark-fill);
    flex: none;
  }
  .brand__name {
    font-family: "Cinzel", serif;
    font-weight: 500;
    font-size: 15px;
    line-height: 1.15;
    letter-spacing: 0.04em;
    text-transform: uppercase;
  }
  .card--front .brand { top: 30px; left: 34px; }
  .card--back .brand { right: 34px; bottom: 60px; }
  .contacts {
    position: absolute;
    left: 34px;
    top: 92px;
    list-style: none;
    font-family: "Lato", sans-serif;
    font-weight: 300;
    font-size: 12.5px;
    line-height: 1.45;
    letter-spacing: 0.02em;
  }
  .contacts__row {
    display: flex;
    align-items: flex-start;
    gap: 16px;
    margin-bottom: 10px;
  }
  .contacts__row:last-child { margin-bottom: 0; }
  .contacts__icon {
    width: 14px;
    height: 14px;
    flex: none;
    margin-top: 2px;
    fill: none;
    stroke: var(--front-ink);
    stroke-width: 1.3;
  }
  .contacts__icon--solid { fill: var(--front-ink); stroke: none; }
  .licence {
    position: absolute;
    left: 64px;
    bottom: 24px;
    font-family: "Lato", sans-serif;
    font-weight: 300;
    font-size: 12px;
    letter-spacing: 0.02em;
  }
</style>
</head>
<body>
<main class="sheet">
  <section class="card card--front" aria-label="Card front">
    <div class="brand">
      <span class="brand__square"></span>
      <span class="brand__name">Bracken Hollow<br>Masonry</span>
    </div>
    <ul class="contacts">
      <li class="contacts__row">
        <svg class="contacts__icon contacts__icon--solid" viewBox="0 0 16 16" aria-hidden="true">
          <path d="M3.5 1.5c.6-.4 1.3-.3 1.7.3l1.4 2.1c.3.5.2 1.1-.2 1.5l-.9.8c.7 1.6 2 2.9 3.6 3.6l.8-.9c.4-.4 1-.5 1.5-.2l2.1 1.4c.6.4.7 1.1.3 1.7l-.8 1.1c-.5.7-1.4 1-2.2.7C6.4 13 3 9.6 1.5 5.2c-.3-.8 0-1.7.7-2.2z"/>
        </svg>
        <span>T 1300517926<br>M 0471926038<br>F 1900 457 618</span>
      </li>
      <li class="contacts__row">
        <svg class="contacts__icon" viewBox="0 0 16 16" aria-hidden="true">
          <rect x="1.5" y="3.5" width="13" height="9"/>
          <path d="M1.5 3.5 8 9l6.5-5.5"/>
        </svg>
        <span>delwyn@brackenhollowmasonry.com.au</span>
      </li>
      <li class="contacts__row">
        <svg class="contacts__icon" viewBox="0 0 16 16" aria-hidden="true">
          <circle cx="8" cy="8" r="6.5"/>
          <ellipse cx="8" cy="8" rx="3" ry="6.5"/>
          <path d="M1.5 8h13"/>
        </svg>
        <span>www.brackenhollowmasonry.com.au</span>
      </li>
      <li class="contacts__row">
        <svg class="contacts__icon" viewBox="0 0 16 16" aria-hidden="true">
          <path d="M8 15s-5-5.2-5-8.6A5 5 0 0 1 13 6.4C13 9.8 8 15 8 15z"/>
          <circle cx="8" cy="6.4" r="1.8"/>
        </svg>
        <span>518/ 217 Wendlebury st Thornvale</span>
      </li>
    </ul>
    <p class="licence">Licence number : 847263k</p>
  </section>

  <section class="card card--back" aria-label="Card back">
    <div class="brand">
      <span class="brand__square"></span>
      <span class="brand__name">Bracken Hollow<br>Masonry</span>
    </div>
  </section>
</main>
</body>
</html>
```